Cosmetic Label Design for a Sunless Tanner

We need a label for a new sunless tanner. The label dye will be 2.5 inches in height by 6 inches in width. It will be laser printed by Brintova.net The label will be printed on gloss laminated white polypropylene self-adhesive material. A full project description can be found in the attached Word file. The label copy is also included in a Word file.

Target Market(s)

Females aged 18 to 35

Font styles to use
Serif

Colors

Designer to choose colors to be used in the design.

Requirements
Must have
• Clean look. Strong brand image.
Nice to have
• This is the first product in a future line. The design should have the ability to move to other products.
Should not have
• Too heavy. More than 4 colors. Fonts that are whimsical. Cursive writing. No cartoon like illustrations.

```html
<!DOCTYPE html>
<html lang="en">
<head>
<meta charset="UTF-8">
<title>Bronzelle Sunless Tanner Label</title>
<link rel="stylesheet" href="https://fonts.googleapis.com/css2?family=EB+Garamond:wght@400;500&display=swap">
<style>
  :root {
    --backdrop: #f1f1f0;
    --gold-light: #f4e7b9;
    --gold-mid: #ead59a;
    --gold-deep: #dcc07a;
    --ornament: #e2bd7e;
    --ink: #c07d28;
    --ink-soft: #b9822f;
    --accent-band: #f0b768;
    --paper: #ffffff;
  }
  * { margin: 0; padding: 0; box-sizing: border-box; }
  html, body {
    width: 1200px;
    height: 1200px;
    overflow: hidden;
    background: var(--backdrop);
  }
  .canvas {
    position: relative;
    width: 1200px;
    height: 1200px;
    display: flex;
    align-items: center;
    justify-content: center;
  }
  .label {
    position: relative;
    width: 1000px;
    height: 417px;
    overflow: hidden;
    background: linear-gradient(100deg, var(--gold-mid) 0%, var(--gold-light) 45%, var(--gold-mid) 75%, var(--gold-deep) 100%);
    box-shadow: 0 6px 24px rgba(0,0,0,0.08);
  }
  .label__ornament {
    position: absolute;
    left: 90px;
    top: -120px;
    width: 760px;
    height: 330px;
    border-radius: 0 0 50% 50%;
    background: radial-gradient(ellipse at center, rgba(226,189,126,0.55) 0%, rgba(226,189,126,0.25) 60%, rgba(226,189,126,0) 100%);
  }
  .label__corner {
    position: absolute;
    right: 0;
    bottom: 0;
    width: 160px;
    height: 200px;
  }
  .label__copy {
    position: absolute;
    left: 0;
    right: 0;
    top: 160px;
    text-align: center;
    font-family: "EB Garamond", serif;
    color: var(--ink);
    text-transform: uppercase;
  }
  .label__certified {
    font-size: 26px;
    letter-spacing: 2px;
    line-height: 1;
    color: var(--ink-soft);
  }
  .label__brand {
    font-size: 52px;
    font-weight: 500;
    letter-spacing: 1px;
    line-height: 1.05;
    margin-top: 4px;
  }
  .label__descriptor {
    font-size: 24px;
    letter-spacing: 1px;
    margin-top: 26px;
    line-height: 1;
    color: var(--ink-soft);
  }
  .label__product {
    font-size: 46px;
    font-weight: 500;
    line-height: 1.1;
    margin-top: 4px;
  }
  .label__meta {
    font-size: 15px;
    letter-spacing: 0.5px;
    margin-top: 30px;
    line-height: 1.4;
    color: var(--ink-soft);
  }
</style>
</head>
<body>
  <main class="canvas">
    <section class="label">
      <div class="label__ornament" role="img" aria-label="Soft gold mandala-style pattern across the top of the label"></div>
      <svg class="label__corner" viewBox="0 0 160 200" aria-hidden="true">
        <path d="M160 40 C120 90 60 140 0 200 L40 200 C90 150 130 120 160 100 Z" fill="var(--accent-band)" opacity="0.7"/>
        <path d="M160 100 C130 120 90 150 40 200 L160 200 Z" fill="var(--gold-deep)"/>
        <path d="M160 140 L160 200 L110 200 C130 180 145 160 160 140 Z" fill="var(--paper)"/>
      </svg>
      <div class="label__copy">
        <p class="label__certified">Certified</p>
        <h1 class="label__brand">Bronzelle</h1>
        <p class="label__descriptor">Skin Nourishing</p>
        <h2 class="label__product">Sunless Tanner</h2>
        <p class="label__meta">Natural Ingredients<br>8 oz</p>
      </div>
    </section>
  </main>
</body>
</html>
```